Business cards and stationery for a software company
Klovarent s.r.o.
Simple
Petr Hrubeš
Lipová alej 2841/9
Praha 5
petr.hrubes@klovarent-example.com
www.klovarent-example.com

```html
<!DOCTYPE html>
<html lang="cs">
<head>
<meta charset="utf-8">
<title>Klovarent s.r.o. – stationery</title>
<link rel="stylesheet" href="https://fonts.googleapis.com/css2?family=Ubuntu:wght@400;700&display=swap">
<style>
  :root {
    --bg: #000000;
    --paper: #ffffff;
    --purple: #7b2d8e;
    --purple-dark: #5a1c6b;
    --purple-light: #a660b8;
    --ink: #3a2a44;
    --gray-card: #3b3939;
    --gray-card-dark: #2a2828;
    --gray-line: #8d8d8d;
  }
  * { margin: 0; padding: 0; box-sizing: border-box; }
  html, body { width: 1200px; height: 749px; overflow: hidden; background: var(--bg); }
  body { font-family: "Ubuntu", Arial, sans-serif; }
  .stage { position: relative; width: 1200px; height: 749px; background: var(--bg); }

  .sheet { position: absolute; background: var(--paper); overflow: hidden; }
  .band { position: absolute; left: 0; bottom: 0; width: 100%; display: block; }

  .brand { position: absolute; display: flex; align-items: center; gap: 8px; }
  .brand-dot { border-radius: 50%; background: var(--purple); flex: none; }
  .brand-name { font-weight: 700; color: var(--purple); letter-spacing: -0.5px; line-height: 1; }

  /* Letterhead */
  .letterhead { left: 58px; top: 29px; width: 514px; height: 684px; }
  .letterhead .brand { left: 22px; top: 42px; }
  .letterhead .brand-dot { width: 30px; height: 30px; }
  .letterhead .brand-name { font-size: 34px; }
  .footer-text { position: absolute; color: var(--paper); font-size: 9px; line-height: 13px; }
  .letterhead .footer-text { left: 22px; bottom: 14px; }

  /* Business card front */
  .card { position: absolute; overflow: hidden; border-radius: 4px; }
  .card-front { left: 588px; top: 31px; width: 209px; height: 123px; background: var(--paper); }
  .card-front .brand { left: 10px; top: 12px; gap: 5px; }
  .card-front .brand-dot { width: 12px; height: 12px; }
  .card-front .brand-name { font-size: 15px; }
  .card-holder { position: absolute; left: 112px; top: 50px; font-size: 7px; color: var(--ink); }
  .card-front .footer-text { left: 10px; bottom: 5px; font-size: 5px; line-height: 6px; }

  /* Card backs */
  .card-back { display: flex; align-items: center; justify-content: center; }
  .card-back .brand { position: static; gap: 6px; }
  .card-back .brand-dot { width: 14px; height: 14px; }
  .card-back .brand-name { font-size: 20px; }
  .card-purple { left: 665px; top: 187px; width: 211px; height: 122px;
    background: linear-gradient(180deg, var(--purple-light), var(--purple) 60%, var(--purple-dark)); }
  .card-purple .brand-dot { background: var(--paper); }
  .card-purple .brand-name { color: var(--paper); }
  .card-white { left: 893px; top: 113px; width: 211px; height: 122px; background: var(--paper); }
  .card-dark { left: 922px; top: 245px; width: 211px; height: 120px;
    background: linear-gradient(180deg, var(--gray-card), var(--gray-card-dark)); }
  .card-dark .brand-dot { background: var(--paper); }
  .card-dark .brand-name { color: var(--paper); }

  /* Envelope */
  .envelope { left: 586px; top: 372px; width: 547px; height: 341px; }
  .envelope-flap { position: absolute; left: 0; top: 0; width: 100%; height: 84px; display: block; }
  .flap-brand { position: absolute; left: 0; top: 22px; width: 100%; display: flex; justify-content: center; }
  .flap-brand .brand-name { color: var(--paper); font-size: 22px; }
  .envelope .brand.main { left: 18px; top: 122px; }
  .envelope .brand.main .brand-dot { width: 28px; height: 28px; }
  .envelope .brand.main .brand-name { font-size: 32px; }
  .envelope .footer-text { left: 18px; bottom: 12px; }
</style>
</head>
<body>
<main class="stage">

  <section class="sheet letterhead" aria-label="Letterhead">
    <div class="brand"><span class="brand-dot"></span><span class="brand-name">klovarent</span></div>
    <svg class="band" width="514" height="130" viewBox="0 0 514 130" preserveAspectRatio="none" aria-hidden="true">
      <defs>
        <linearGradient id="lhBand" x1="0" y1="0" x2="0" y2="1">
          <stop offset="0" stop-color="#a660b8"/><stop offset="1" stop-color="#6a2480"/>
        </linearGradient>
      </defs>
      <path d="M0 14 C160 70 360 78 514 20" fill="none" stroke="#8d8d8d" stroke-width="3"/>
      <path d="M0 26 C160 82 360 90 514 32 L514 130 L0 130 Z" fill="url(#lhBand)"/>
      <path d="M0 26 C160 82 360 90 514 32 L514 40 C360 96 160 92 0 36 Z" fill="#ffffff" opacity="0.5"/>
    </svg>
    <p class="footer-text">Lipová alej 2841/9, Praha 5<br>Phone: +420 601 234 567<br>Email: petr.hrubes@klovarent-example.com / www.klovarent-example.com</p>
  </section>

  <section class="card card-front" aria-label="Business card front">
    <div class="brand"><span class="brand-dot"></span><span class="brand-name">klovarent</span></div>
    <p class="card-holder">Petr Hrubeš</p>
    <svg class="band" width="209" height="56" viewBox="0 0 209 56" preserveAspectRatio="none" aria-hidden="true">
      <path d="M0 4 C70 18 150 20 209 6" fill="none" stroke="#8d8d8d" stroke-width="1.5"/>
      <path d="M0 9 C70 23 150 25 209 11 L209 56 L0 56 Z" fill="#7b2d8e"/>
    </svg>
    <p class="footer-text">Lipová alej 2841/9, Praha 5<br>Phone: +420 601 234 567<br>petr.hrubes@klovarent-example.com / www.klovarent-example.com</p>
  </section>

  <section class="card card-back card-purple" aria-label="Business card back, purple">
    <div class="brand"><span class="brand-dot"></span><span class="brand-name">klovarent</span></div>
  </section>

  <section class="card card-back card-white" aria-label="Business card back, white">
    <div class="brand"><span class="brand-dot"></span><span class="brand-name">klovarent</span></div>
  </section>

  <section class="card card-back card-dark" aria-label="Business card back, dark">
    <div class="brand"><span class="brand-dot"></span><span class="brand-name">klovarent</span></div>
  </section>

  <section class="sheet envelope" aria-label="Envelope">
    <svg class="envelope-flap" width="547" height="84" viewBox="0 0 547 84" preserveAspectRatio="none" aria-hidden="true">
      <defs>
        <linearGradient id="flap" x1="0" y1="0" x2="0" y2="1">
          <stop offset="0" stop-color="#a660b8"/><stop offset="1" stop-color="#6a2480"/>
        </linearGradient>
      </defs>
      <path d="M0 84 L0 14 Q0 0 14 0 L533 0 Q547 0 547 14 L547 84 Z" fill="url(#flap)"/>
      <path d="M0 80 L547 80 L547 84 L0 84 Z" fill="#4a1558"/>
    </svg>
    <div class="flap-brand"><span class="brand-name">klovarent</span></div>
    <div class="brand main"><span class="brand-dot"></span><span class="brand-name">klovarent</span></div>
    <svg class="band" width="547" height="96" viewBox="0 0 547 96" preserveAspectRatio="none" aria-hidden="true">
      <path d="M0 8 C170 54 380 60 547 12" fill="none" stroke="#8d8d8d" stroke-width="3"/>
      <path d="M0 18 C170 64 380 70 547 22 L547 96 L0 96 Z" fill="url(#lhBand)"/>
      <path d="M0 18 C170 64 380 70 547 22 L547 29 C380 76 170 72 0 26 Z" fill="#ffffff" opacity="0.5"/>
    </svg>
    <p class="footer-text">Lipová alej 2841/9, Praha 5</p>
  </section>

</main>
</body>
</html>
```